Business card and stationary designs for Harbor Summit Mentor
Harbor Summit Mentor
Business card and stationary designs for Harbor Summit Mentor - Consulting
Creative Brief
Professional
Reed Calloway
Executive & Professional Coach
4187 Willow Bend Lane Dallas TX 75231
RCalloway@harborsummitmentor.example
www.HarborSummitMentor.example
I want this to look clean, cutting edge, and for the design to stand out.
On the back of the business card I would like my logo and the phrase "Executive & Professional Coaching"

```html
<!DOCTYPE html>
<html lang="en">
<head>
<meta charset="utf-8">
<title>Harbor Summit Mentor — Business Cards</title>
<link rel="stylesheet" href="https://fonts.googleapis.com/css2?family=Cinzel:wght@400;600&family=Montserrat:wght@400;500;600&display=swap">
<style>
  :root {
    --backdrop: #e6e3df;
    --card: #ffffff;
    --ink: #1b1b1b;
    --ink-soft: #4a4a4a;
    --band: #111111;
    --accent-grey: #a9a9a9;
    --rule: #2a2a2a;
  }
  * { box-sizing: border-box; margin: 0; padding: 0; }
  html, body {
    width: 1200px; height: 904px; overflow: hidden;
    background: var(--backdrop);
    font-family: "Montserrat", Arial, sans-serif;
    color: var(--ink);
  }
  .stage {
    position: relative; width: 1200px; height: 904px;
    display: flex; flex-direction: column; align-items: center;
    justify-content: center; gap: 40px;
  }
  .card {
    position: relative; width: 700px; height: 400px;
    background: var(--card);
    box-shadow: 0 10px 30px rgba(0,0,0,0.18);
    overflow: hidden;
  }

  /* Front */
  .card-front { display: flex; flex-direction: column; align-items: center; justify-content: center; }
  .brand { display: flex; align-items: center; gap: 14px; }
  .brand-dot {
    width: 22px; height: 22px; border-radius: 50%;
    background: var(--ink);
  }
  .brand-name {
    font-family: "Cinzel", Georgia, serif;
    font-weight: 600; letter-spacing: 2px; color: var(--ink);
  }
  .card-front .brand-name { font-size: 34px; }
  .front-web {
    margin-top: 34px; font-size: 14px; letter-spacing: 1.5px;
    color: var(--ink-soft);
  }

  /* Back */
  .back-brand { position: absolute; left: 200px; top: 62px; }
  .back-brand .brand-name { font-size: 26px; }
  .back-brand .brand-dot { width: 18px; height: 18px; }
  .top-rule {
    position: absolute; left: 0; right: 0; top: 128px;
    height: 2px; background: var(--rule);
  }
  .grey-block {
    position: absolute; right: 0; top: 128px; width: 140px; height: 50px;
    background: var(--accent-grey);
  }
  .name-band {
    position: absolute; left: 0; right: 0; top: 178px; height: 72px;
    background: var(--band); color: #fff;
    display: flex; flex-direction: column; align-items: center; justify-content: center;
    gap: 6px; padding-right: 80px;
  }
  .person-name { font-size: 20px; font-weight: 600; letter-spacing: 1px; }
  .person-title { font-size: 13px; font-weight: 400; letter-spacing: 1px; color: #dcdcdc; }
  .contact {
    position: absolute; left: 60px; right: 60px; top: 276px;
    list-style: none; display: flex; flex-direction: column; align-items: center; gap: 9px;
    font-size: 13px; color: var(--ink-soft);
  }
  .contact-row { display: flex; align-items: center; gap: 10px; }
  .contact-item { display: inline-flex; align-items: center; gap: 6px; }
  .contact-sep { color: var(--accent-grey); }
  .icon { width: 14px; height: 14px; fill: var(--ink); }
</style>
</head>
<body>
<main class="stage">
  <section class="card card-front" aria-label="Business card front">
    <div class="brand">
      <span class="brand-dot"></span>
      <span class="brand-name">Harbor Summit Mentor</span>
    </div>
    <p class="front-web">www.harborsummitmentor.example</p>
  </section>

  <section class="card card-back" aria-label="Business card back">
    <div class="brand back-brand">
      <span class="brand-dot"></span>
      <span class="brand-name">Harbor Summit Mentor</span>
    </div>
    <div class="top-rule"></div>
    <div class="grey-block"></div>
    <div class="name-band">
      <span class="person-name">Reed Calloway</span>
      <span class="person-title">Executive &amp; Professional Coach</span>
    </div>
    <ul class="contact">
      <li class="contact-row">4187 Willow Bend Lane Dallas TX 75231</li>
      <li class="contact-row">
        <span class="contact-item">
          <svg class="icon" viewBox="0 0 24 24" aria-hidden="true"><path d="M6.6 10.8a15 15 0 0 0 6.6 6.6l2.2-2.2a1 1 0 0 1 1-.25 11.4 11.4 0 0 0 3.6.57 1 1 0 0 1 1 1V20a1 1 0 0 1-1 1A17 17 0 0 1 3 4a1 1 0 0 1 1-1h3.5a1 1 0 0 1 1 1c0 1.25.2 2.45.57 3.6a1 1 0 0 1-.25 1z"/></svg>
          1-800-555-0148
        </span>
        <span class="contact-sep">|</span>
        <span class="contact-item">
          <svg class="icon" viewBox="0 0 24 24" aria-hidden="true"><path d="M7 1h10a2 2 0 0 1 2 2v18a2 2 0 0 1-2 2H7a2 2 0 0 1-2-2V3a2 2 0 0 1 2-2zm0 4v13h10V5zm5 14.5a1 1 0 1 0 0 2 1 1 0 0 0 0-2z"/></svg>
          214-555-0193
        </span>
        <span class="contact-sep">|</span>
        <span class="contact-item">
          <svg class="icon" viewBox="0 0 24 24" aria-hidden="true"><path d="M2 5h20v14H2zm2 2v.5l8 5 8-5V7zm0 3v7h16v-7l-8 5z"/></svg>
          RCalloway@harborsummitmentor.example
        </span>
      </li>
      <li class="contact-row">
        <span class="contact-item">
          <svg class="icon" viewBox="0 0 24 24" aria-hidden="true"><path d="M12 2a10 10 0 1 0 0 20 10 10 0 0 0 0-20zm6.9 6h-2.9a15 15 0 0 0-1.4-3.6A8 8 0 0 1 18.9 8zM12 4c.8 1.2 1.5 2.5 1.9 4h-3.8c.4-1.5 1.1-2.8 1.9-4zM4.3 14a8 8 0 0 1 0-4h3.4a16 16 0 0 0 0 4zm.8 2h2.9c.3 1.3.8 2.5 1.4 3.6A8 8 0 0 1 5.1 16zM8 8H5.1a8 8 0 0 1 4.3-3.6C8.8 5.5 8.4 6.7 8 8zm4 12c-.8-1.2-1.5-2.5-1.9-4h3.8c-.4 1.5-1.1 2.8-1.9 4zm2.3-6H9.7a14 14 0 0 1 0-4h4.6a14 14 0 0 1 0 4zm.3 5.6c.6-1.1 1.1-2.3 1.4-3.6h2.9a8 8 0 0 1-4.3 3.6zm1.7-5.6a16 16 0 0 0 0-4h3.4a8 8 0 0 1 0 4z"/></svg>
          www.HarborSummitMentor.example
        </span>
      </li>
    </ul>
  </section>
</main>
</body>
</html>
```